DLB / WLB

I need a business card for the owner of sister companies. Please see minimalist version of our old business card for just the Quillmere business. We need to now have a card that shows off both the Quillmere logo and the Willow Lane Builders logo. We would like the aesthetic to go well with our brand, and not differ greatly from our Quillmere cards. These companies are sister companies, there is not one parent company. Looking for a visually appealing design, but not sure if it should be diagonal or something to make it visually attractive... or just some other type of divider. We prefer white logos with a blue background. White transparent background png logos are attached. Please use blue background with hex code 566b7c. The person and contact information will be on the back side, and I can do that myself. We will NOT need to add the text for design-build-sales-installation.

```html
<!DOCTYPE html>
<html lang="en">
<head>
<meta charset="utf-8">
<title>DLB / WLB Business Card</title>
<link href="https://fonts.googleapis.com/css2?family=Poppins:wght@400;700&display=swap" rel="stylesheet">
<style>
  :root {
    --card-blue: #566b7c;
    --ink-white: #ffffff;
    --stage: #e9e6e1;
    --rule: rgba(255,255,255,0.55);
  }
  * { box-sizing: border-box; margin: 0; padding: 0; }
  html, body { width: 1200px; height: 900px; overflow: hidden; }
  body {
    background: var(--stage);
    font-family: "Poppins", sans-serif;
    color: var(--ink-white);
    position: relative;
  }
  .card {
    position: absolute;
    left: 290px;
    width: 620px;
    height: 354px;
    background: var(--card-blue);
    border-radius: 34px;
    box-shadow: 0 6px 18px rgba(0,0,0,0.18);
  }
  .card--back { top: 50px; }
  .card--front { top: 470px; }

  .brand {
    display: flex;
    align-items: center;
    gap: 10px;
    font-weight: 700;
    line-height: 1.1;
    white-space: nowrap;
  }
  .brand__mark {
    width: 20px; height: 20px;
    background: var(--ink-white);
    flex: none;
  }
  .brand__name { font-size: 21px; }

  .block { position: absolute; }
  .block--left { left: 44px; text-align: left; }
  .block--right { right: 44px; text-align: right; }
  .block--right .brand { justify-content: flex-end; }

  .brand-left { top: 118px; }
  .brand-right { top: 36px; }
  .person-left { top: 212px; }
  .person-right { top: 126px; }
  .contacts-left { top: 272px; }
  .contacts-right { top: 186px; }

  .person__name { font-weight: 700; font-size: 17px; letter-spacing: 0.5px; line-height: 1.3; }
  .person__role { font-size: 15px; font-weight: 400; line-height: 1.3; }

  .contacts { list-style: none; font-size: 14.5px; }
  .contacts li { display: flex; align-items: center; gap: 8px; line-height: 1.45; white-space: nowrap; }
  .block--right .contacts li { justify-content: flex-end; }
  .contacts svg { width: 13px; height: 13px; flex: none; }

  .front-lockup {
    position: absolute; inset: 0;
    display: flex; align-items: center; justify-content: center; gap: 30px;
  }
  .front-lockup .brand__name { font-size: 24px; }
  .front-lockup .brand__mark { width: 22px; height: 22px; }
  .divider { width: 1px; height: 110px; background: var(--rule); }
</style>
</head>
<body>

<section class="card card--back" aria-label="Card back with contact details">
  <div class="block block--left brand-left">
    <div class="brand"><span class="brand__mark"></span><span class="brand__name">Willow Lane Builders</span></div>
  </div>
  <div class="block block--left person-left">
    <p class="person__name">RUTH CALDER</p>
    <p class="person__role">Owner</p>
  </div>
  <ul class="block block--left contacts contacts-left">
    <li><svg viewBox="0 0 24 24" fill="#fff"><path d="M6.6 10.8a15 15 0 0 0 6.6 6.6l2.2-2.2c.3-.3.7-.4 1-.2 1.1.4 2.3.6 3.6.6.6 0 1 .4 1 1V20c0 .6-.4 1-1 1A17 17 0 0 1 3 4c0-.6.4-1 1-1h3.5c.6 0 1 .4 1 1 0 1.3.2 2.5.6 3.6.1.3 0 .7-.2 1z"/></svg>555-014-7720</li>
    <li><svg viewBox="0 0 24 24" fill="#fff"><path d="M2 5h20v14H2z M2 5l10 8 10-8" stroke="#566b7c" stroke-width="1.6"/></svg>info@willowlanebuilders.com</li>
    <li><svg viewBox="0 0 24 24" fill="none" stroke="#fff" stroke-width="2"><circle cx="12" cy="12" r="9"/><path d="M3 12h18M12 3c3 3 3 15 0 18M12 3c-3 3-3 15 0 18"/></svg>www.willowlanebuilders.com</li>
  </ul>

  <div class="block block--right brand-right">
    <div class="brand"><span class="brand__mark"></span><span class="brand__name">Quillmere</span></div>
  </div>
  <div class="block block--right person-right">
    <p class="person__name">NORA CALDER</p>
    <p class="person__role">Owner</p>
  </div>
  <ul class="block block--right contacts contacts-right">
    <li>555-014-7720<svg viewBox="0 0 24 24" fill="#fff"><path d="M6.6 10.8a15 15 0 0 0 6.6 6.6l2.2-2.2c.3-.3.7-.4 1-.2 1.1.4 2.3.6 3.6.6.6 0 1 .4 1 1V20c0 .6-.4 1-1 1A17 17 0 0 1 3 4c0-.6.4-1 1-1h3.5c.6 0 1 .4 1 1 0 1.3.2 2.5.6 3.6.1.3 0 .7-.2 1z"/></svg></li>
    <li>info@Quillmere.com<svg viewBox="0 0 24 24" fill="#fff"><path d="M2 5h20v14H2z M2 5l10 8 10-8" stroke="#566b7c" stroke-width="1.6"/></svg></li>
    <li>www.Quillmere.com<svg viewBox="0 0 24 24" fill="none" stroke="#fff" stroke-width="2"><circle cx="12" cy="12" r="9"/><path d="M3 12h18M12 3c3 3 3 15 0 18M12 3c-3 3-3 15 0 18"/></svg></li>
  </ul>
</section>

<section class="card card--front" aria-label="Card front with both company names">
  <div class="front-lockup">
    <div class="brand"><span class="brand__mark"></span><span class="brand__name">Willow Lane Builders</span></div>
    <span class="divider"></span>
    <div class="brand"><span class="brand__mark"></span><span class="brand__name">Quillmere</span></div>
  </div>
</section>

</body>
</html>
```